Book Title: “Ember: Road of Quiet Dawn” Please see the attachment “Text on the cover”.

Book Cover Design Instructions: This book is meant for people of all religions and nationalities. Therefore, on the cover, there should be no mosque or an object specific to any religion. The primary emphasis should be on the "unconditional love of God." Therefore, use universal symbols of love. The second priority themes could be Sufism, Peace, and self-improvement. Rest is your imagination. Please also see the attachment: 'Book description and author's Bio.'
This book has the potential to be a best seller. Please do a good job.
What Book Cover Formats are required: A designer should submit cover designs in three formats: (1) eBook, (2) Paperback, and (3) Hardback. These books will be published on Velmora PBX.
Format requirements for eBooks are available from: https://pbx.velmora-press.example/en_US/help/topic/R731928405.
You can find paperback and hardback cover measurements from: https://pbx.velmora-press.example/en_US/cover-calculator
• To complete the project, all three formats should be accepted by Velmora PBX.
• The book interior trim size is 6.14 X 9.21 inches.
• Interior Type: Premium color.
• No bleed.
• I do not upload barcode. So, the back cover should have room for Velmora to print the barcode.
• Number of pages 126.
Compensation for the designer: After selecting one designer, I will increase the amount by $200 on Artlumo to compensate for three deliverables.
Follow-up of the Project:
After the book is published, I may need minor revisions. For example, the number of pages may change. Therefore, I will need the same design in revised sizes. In that case, I will pay $25 for each revision. For example, if the number of pages changes, I will need a different spine for paperback and hardback, then I will pay the artist $25 + $25 = $50 for both designs.
List of Enclosers:
1. Text on the cover.
2. Book description and author's Bio for the back cover.
3. Later, I will upload my picture for the book's back cover.

Target Market(s)

Any adult

Industry/Entity Type

Any industry

Requirements
Must have
• Three Deliverables

```html
<!DOCTYPE html>
<html lang="en">
<head>
<meta charset="utf-8">
<title>Ember: Road of Quiet Dawn — Cover Wrap</title>
<link href="https://fonts.googleapis.com/css2?family=Cinzel:wght@400;600;700&family=Montserrat:wght@400;500&display=swap" rel="stylesheet">
<style>
  :root {
    --backdrop: #000000;
    --gold-light: #e9cf86;
    --gold-mid: #c59b45;
    --gold-deep: #9c7530;
    --gold-ink: #a8823c;
    --sky-top: #a9b6d6;
    --sky-mid: #c9cee0;
    --body-ink: #1b1b22;
    --paper: #ffffff;
  }
  * { margin: 0; padding: 0; box-sizing: border-box; }
  html, body { width: 1200px; height: 1200px; overflow: hidden; background: var(--backdrop); }
  .canvas { position: relative; width: 1200px; height: 1200px; }

  .wrap { position: absolute; left: 49px; top: 205px; width: 1102px; height: 791px; }

  .sky { position: absolute; top: 0; height: 100%; }
  .sky--back {
    left: 0; width: 531px;
    background:
      radial-gradient(ellipse at 70% 20%, rgba(255,255,255,.55), transparent 45%),
      radial-gradient(ellipse at 30% 85%, rgba(240,236,236,.8), transparent 50%),
      radial-gradient(ellipse at 90% 70%, rgba(235,230,232,.7), transparent 45%),
      linear-gradient(180deg, var(--sky-top) 0%, var(--sky-mid) 50%, #d3d5e2 100%);
  }
  .sky--front {
    left: 571px; width: 531px;
    background:
      radial-gradient(ellipse at 55% 30%, rgba(255,248,225,.95) 0%, rgba(255,240,205,.6) 20%, transparent 50%),
      radial-gradient(ellipse at 50% 75%, rgba(245,232,225,.9), transparent 55%),
      radial-gradient(ellipse at 10% 55%, rgba(240,232,232,.7), transparent 40%),
      linear-gradient(180deg, #9fb1d4 0%, #d7d4dc 45%, #c9c6d6 80%, #8f99b7 100%);
  }

  .gold-fill {
    background: linear-gradient(180deg, var(--gold-light) 0%, var(--gold-mid) 45%, var(--gold-deep) 100%);
    -webkit-background-clip: text; background-clip: text; color: transparent;
  }

  /* back cover */
  .back { position: absolute; left: 0; top: 0; width: 531px; height: 100%; }
  .back__title {
    position: absolute; left: 34px; top: 34px; width: 463px;
    font-family: "Cinzel", serif; font-weight: 400; font-size: 29px; letter-spacing: .3px;
    color: var(--gold-ink); white-space: nowrap;
  }
  .back__subtitle {
    position: absolute; left: 34px; top: 78px; width: 463px;
    font-family: "Cinzel", serif; font-weight: 600; font-size: 13.6px;
    color: var(--gold-ink); white-space: nowrap;
  }
  .back__blurb {
    position: absolute; left: 34px; top: 100px; width: 463px;
    font-family: "Montserrat", sans-serif; font-size: 11.2px; line-height: 12.7px;
    color: var(--body-ink); text-align: justify;
  }
  .back__blurb p { margin-bottom: 12.7px; }
  .back__blurb p.tight { text-align: left; }

  .author-photo-slot {
    position: absolute; left: 34px; top: 546px; width: 134px; height: 169px;
    background: var(--paper); border: 1px solid var(--gold-mid);
  }
  .back__author {
    position: absolute; left: 185px; top: 546px;
    font-family: "Cinzel", serif; font-weight: 400; font-size: 20px; color: var(--gold-ink);
  }
  .back__bio {
    position: absolute; left: 185px; top: 578px; width: 312px;
    font-family: "Montserrat", sans-serif; font-size: 11.2px; line-height: 12.7px;
    color: var(--body-ink); text-align: justify;
  }
  .barcode-space {
    position: absolute; left: 306px; top: 657px; width: 192px; height: 104px;
    background: var(--paper); border: 1px solid var(--gold-mid);
  }

  /* spine */
  .spine {
    position: absolute; left: 531px; top: 0; width: 40px; height: 100%;
    background: linear-gradient(90deg, #b38a3e 0%, #e6cb86 35%, #d8b768 60%, #a77e34 100%);
  }
  .spine__title, .spine__author {
    position: absolute; left: 50%;
    font-family: "Cinzel", serif; font-size: 22px; color: var(--gold-deep);
    white-space: nowrap; transform-origin: 0 0;
    transform: rotate(90deg) translateY(-50%);
  }
  .spine__title { top: 40px; }
  .spine__author { top: 534px; }

  /* front cover */
  .front { position: absolute; left: 571px; top: 0; width: 531px; height: 100%; }
  .front__title {
    position: absolute; left: 0; top: 28px; width: 100%; text-align: center;
    font-family: "Cinzel", serif; font-weight: 600; line-height: 1;
    filter: drop-shadow(0 1px 1px rgba(90,60,20,.35));
  }
  .front__title span { display: block; }
  .front__title .line-1 { font-size: 104px; letter-spacing: 2px; }
  .front__title .line-2 { font-size: 80px; margin-top: -6px; }
  .front__title .line-3 { font-size: 56px; margin-top: -2px; }

  .front__subtitle {
    position: absolute; left: 0; top: 412px; width: 100%; text-align: center;
    font-family: "Cinzel", serif; font-weight: 700; font-style: italic;
    font-size: 25px; line-height: 34px;
    filter: drop-shadow(0 1px 1px rgba(90,60,20,.4));
  }

  .author-band {
    position: absolute; left: 0; bottom: 0; width: 100%; height: 74px;
    background: linear-gradient(180deg, #c89f4e 0%, #ecd48e 40%, #dcbc6c 70%, #b8913f 100%);
    display: flex; align-items: center; justify-content: center;
  }
  .author-band__name {
    font-family: "Cinzel", serif; font-size: 28px; letter-spacing: 1px; color: var(--gold-deep);
  }
</style>
</head>
<body>
<div class="canvas">
  <div class="wrap">
    <div class="sky sky--back" role="img" aria-label="Soft sky of pale blue and white clouds with faint stars"></div>
    <div class="sky sky--front" role="img" aria-label="Radiant heavenly cloudscape with golden light beams and sparkling stars"></div>

    <section class="back">
      <h2 class="back__title">EMBER: ROAD OF QUIET DAWN</h2>
      <h3 class="back__subtitle">HANDBOOK FOR NURTURING A CALM HEART AND GENTLE DAYS</h3>
      <div class="back__blurb">
        <p>This book weaves together the many teachings of Sufism with the deep wisdom of scripture to offer a clear roadmap for personal spiritual growth. Readers are invited to taste for themselves the quiet peace and boundless love that seekers have treasured for centuries. Along the way, the book takes up these essential questions:</p>
        <p>How can one love God without condition? It is the highest of all loves, and it sparks a deep and transforming spiritual journey.</p>
        <p class="tight">How to sense the love of God, which brings lasting calm and contentment.</p>
        <p class="tight">How to love yourself without condition, which supports growth and harmony.</p>
        <p>What is the wisest way to meet life’s hardest crises so that suffering eases and healing comes sooner?</p>
        <p>The book also examines the strong emphasis on avoiding Zulm (oppression and injustice), a word that appears an astounding 291 times in scripture. Avoiding Zulm in every human dealing should be the first priority for every believer.</p>
        <p>The Teacher Halvaren did not only speak of peace and love. He showed it in practice when he came to lead the city of Medina without bloodshed. He held no inherited throne, and Medina was home to many faiths. Arguably, it was history’s first large-scale peaceful transfer of power.</p>
        <p>In the same spirit, he signed the Treaty of Hudaybia with his fiercest rival, choosing a bold peaceful path to end without violence a bitter war that had cost hundreds of lives.</p>
        <p>Above all, the book lays out a method, in practical steps, for reaching a fully settled and contented soul (Nafs-e-Mutma’inna), the aim of every traveler on the Sufi path.</p>
      </div>

      <div class="author-photo-slot"></div>
      <h4 class="back__author">DR. IDRIS VARELL</h4>
      <p class="back__bio">Dr. Varell studied physics and computer science and spent many years building software. He later completed a doctorate in comparative spirituality and helped found a community center in Oregon.</p>
      <div class="barcode-space"></div>
    </section>

    <div class="spine">
      <span class="spine__title">EMBER: ROAD OF QUIET DAWN</span>
      <span class="spine__author">DR. IDRIS VARELL</span>
    </div>

    <section class="front">
      <h1 class="front__title">
        <span class="line-1 gold-fill">EMBER</span>
        <span class="line-2 gold-fill">ROAD OF</span>
        <span class="line-3 gold-fill">QUIET DAWN</span>
      </h1>
      <p class="front__subtitle gold-fill">Handbook for Nurturing<br>a Calm Heart and Gentle Days</p>
      <div class="author-band"><span class="author-band__name">DR. IDRIS VARELL</span></div>
    </section>
  </div>
</div>
</body>
</html>
```